Brovana Landing Web Page

We need a web design for a new company head quartered in Philadelphia, PA with satellite offices in San Francisco, CA and New York, NY.
We have a logo and can provide the logo image file.
Here is some information on who we are:
Brovana
Growing information technology companies with experience
About Us: Brovana is an information technology incubator. We cultivate and groom start-ups from concept to reality to profitability. Brovana is managed and owned by entrepreneurs and technologists with proven start-up success. We seek to leverage synergies between our companies which foster innovation, stimulate creativity, increase productivity, streamline operational processes, and facilitate opportunity.
Brovana Companies:
• Brovana Health (should hyperlink to Brovana Health About Us section)
• Brovana IT Services and Staffing (should hyperlink to Brovana IT Services and Staffing About Us section)
Target Market(s)
Healthcare
Industry/Entity Type
Information Technology
Look and feel

```html
<!DOCTYPE html>
<html lang="en">
<head>
<meta charset="utf-8">
<title>Brovana Landing Web Page</title>
<link href="https://fonts.googleapis.com/css2?family=Open+Sans:wght@400;600;700&display=swap" rel="stylesheet">
<style>
  :root{
    --blue-dark:#0a6a98;
    --blue:#0d7fb3;
    --blue-light:#1a9ad3;
    --teal:#1b8fb9;
    --navy:#0d5f8c;
    --text:#333333;
    --muted:#777777;
    --header-bg:#f7f7f7;
    --content-bg:#f2f2f2;
    --card-bg:#f6f6f6;
    --footer:#3a3a3a;
    --footer-dark:#2b2b2b;
    --white:#ffffff;
  }
  *{box-sizing:border-box;margin:0;padding:0}
  html,body{width:1145px;height:1200px;overflow:hidden}
  body{position:relative;background:var(--header-bg);font-family:"Open Sans",Arial,sans-serif;color:var(--text)}
  a{color:inherit;text-decoration:none}

  .top-strip{position:absolute;left:0;top:0;width:1145px;height:11px;background:var(--blue-dark)}

  .brand{position:absolute;left:48px;top:58px;display:flex;align-items:center;gap:14px}
  .brand-mark{width:64px;height:64px;background:var(--blue)}
  .brand-name{font-size:44px;font-weight:600;color:var(--blue);letter-spacing:1px}

  .search{position:absolute;left:908px;top:52px;width:185px;height:27px;background:var(--white);border:1px solid #cfcfcf;box-shadow:1px 1px 2px rgba(0,0,0,.15);font-size:11px;font-style:italic;color:#999;padding:5px 14px}
  .search svg{position:absolute;right:7px;top:6px}
  .follow{position:absolute;left:922px;top:104px;font-size:12px;font-style:italic;color:#888}
  .social{position:absolute;top:98px;width:28px;height:28px;border-radius:2px}
  .social.one{left:1021px;background:#3b5b97}
  .social.two{left:1062px;background:#4cb3e4}

  .nav{position:absolute;left:0;top:169px;width:1145px;height:59px;background:linear-gradient(#1585b8,#0a6896);border-top:1px solid #0a5f88;border-bottom:1px solid #0a5f88}
  .nav a{position:absolute;top:0;height:57px;line-height:57px;text-align:center;color:var(--white);font-size:14px;border-right:1px solid #0a5a80}
  .nav a.active{background:linear-gradient(#27a7de,#168ec6);color:#0b2a3a;font-weight:600}

  .hero{position:absolute;left:48px;top:241px;width:1046px;height:326px;border:1px solid #666;overflow:hidden}
  .hero-photo{position:absolute;inset:0;background:linear-gradient(90deg,#cddde9 0%,#dfe8f0 35%,#eef3f7 65%,#f9fbfc 100%)}
  .hero-caption{position:absolute;left:681px;top:182px;color:#3d3d3d}
  .hero-caption .line1{font-size:22px}
  .hero-caption .line2{font-size:33px;margin-top:2px}
  .hero-dots{position:absolute;left:426px;top:288px}
  .hero-shade{position:absolute;left:70px;top:560px;width:1000px;height:36px;background:radial-gradient(ellipse at 50% 0,rgba(0,0,0,.45),rgba(0,0,0,0) 70%)}

  .content{position:absolute;left:0;top:617px;width:1145px;height:501px;background:var(--content-bg)}

  .welcome-title{position:absolute;left:55px;top:647px;font-size:24px;font-weight:400;color:var(--teal)}
  .welcome-title span{color:var(--navy)}
  .welcome-text{position:absolute;left:55px;top:697px;width:742px;font-size:12.6px;line-height:24px;text-align:justify}

  .company-btn{position:absolute;left:840px;width:233px;background:linear-gradient(#2aa3d8,#0e74a8);border-radius:3px;color:var(--white);font-weight:600;font-size:16px;box-shadow:0 2px 3px rgba(0,0,0,.25)}
  .company-btn.health{top:656px;height:43px;line-height:43px;padding-left:74px}
  .company-btn.staffing{top:720px;height:65px;padding:10px 0 0 59px;line-height:24px;background:linear-gradient(#1480b5,#0b5f8f)}
  .btn-icon{position:absolute;left:-2px;top:50%;transform:translateY(-50%)}

  .card{position:absolute;top:818px;height:276px;background:var(--card-bg);box-shadow:0 1px 3px rgba(0,0,0,.2)}
  .card h2{position:absolute;left:21px;top:12px;font-size:24px;font-weight:400;color:var(--teal)}
  .card h2 span{color:var(--navy)}
  .card .rule{position:absolute;left:22px;top:53px;width:230px;border-top:2px dotted #777}
  .card ul{position:absolute;left:27px;top:62px;list-style:none}
  .card li{font-size:13.6px;height:35px;line-height:35px;padding-left:20px;position:relative}
  .card li::before{content:"";position:absolute;left:0;top:15px;width:5px;height:5px;border-radius:50%;background:#999}
  .card .intro{position:absolute;left:23px;top:72px;width:236px;font-size:12px;line-height:22px;text-align:justify;color:#444}
  .card.staffing ul{top:142px}

  .footer-links{position:absolute;left:0;top:1118px;width:1145px;height:46px;background:var(--footer);color:#e6e6e6;font-size:12px;text-align:center;line-height:46px}
  .footer-links .sep{margin:0 10px}
  .footer-copy{position:absolute;left:0;top:1164px;width:1145px;height:36px;background:var(--footer-dark);color:#e6e6e6;font-size:12px;text-align:center;line-height:36px}
</style>
</head>
<body>
  <div class="top-strip"></div>

  <div class="brand">
    <div class="brand-mark"></div>
    <div class="brand-name">Brovana</div>
  </div>

  <div class="search">Search
    <svg width="13" height="13" viewBox="0 0 13 13"><circle cx="5" cy="5" r="3.8" fill="none" stroke="#aaa" stroke-width="1.4"/><line x1="8" y1="8" x2="12" y2="12" stroke="#aaa" stroke-width="1.6"/></svg>
  </div>
  <div class="follow">Follow us with :</div>
  <a class="social one" href="#" aria-label="Social link"></a>
  <a class="social two" href="#" aria-label="Social link"></a>

  <nav class="nav">
    <a class="active" href="#" style="left:49px;width:116px">HOME</a>
    <a href="#" style="left:165px;width:129px">ABOUT US</a>
    <a href="#" style="left:294px;width:153px">OUR SERVICES</a>
    <a href="#" style="left:447px;width:172px">OUR COMPANIES</a>
    <a href="#" style="left:619px;width:152px">LATEST NEWS</a>
    <a href="#" style="left:771px;width:134px">CONTACT US</a>
    <a href="#" style="left:905px;width:175px;border-right:none">MEMBER LOGIN</a>
  </nav>

  <div class="hero-shade"></div>
  <section class="hero">
    <div class="hero-photo" role="img" aria-label="Photo of a smiling businesswoman in a dark suit in a bright office"></div>
    <div class="hero-caption">
      <div class="line1">Vivamus feugiat egestas lacus,</div>
      <div class="line2">vitae pulvinar tellus</div>
    </div>
    <svg class="hero-dots" width="226" height="38" viewBox="0 0 226 38">
      <path d="M0 38 L20 4 Q22 0 28 0 L198 0 Q204 0 206 4 L226 38 Z" fill="#2f2f2f"/>
      <circle cx="62" cy="18" r="7" fill="#f2f2f2"/>
      <circle cx="91" cy="18" r="7" fill="#151515"/>
      <circle cx="120" cy="18" r="7" fill="#151515"/>
      <circle cx="149" cy="18" r="7" fill="#151515"/>
    </svg>
  </section>

  <main class="content"></main>

  <h1 class="welcome-title">Welcome to <span>Brovana</span></h1>
  <p class="welcome-text">Brovana is an information technology incubator. We cultivate and groom start-ups from concept to reality to profitability. Brovana is managed and owned by entrepreneurs and technologists with proven start-up success. We seek to leverage synergies between our companies which foster innovation, stimulate creativity, increase productivity, streamline operational processes, and facilitate opportunity.</p>

  <a class="company-btn health" href="#health">
    <svg class="btn-icon" width="46" height="46" viewBox="0 0 46 46"><circle cx="23" cy="23" r="21" fill="#bfe6f6" stroke="#ffffff" stroke-width="2"/><path d="M18 10h10v8h8v10h-8v8H18v-8h-8V18h8z" fill="#ffffff" stroke="#7cc7e6"/></svg>
    BROVANA HEALTH
  </a>
  <a class="company-btn staffing" href="#staffing">
    <div class="btn-icon" role="img" aria-label="Illustration of a businessman" style="left:0;width:52px;height:62px;background:linear-gradient(#5a6470,#2e3640);border-radius:4px"></div>
    BROVANA IT SERVICES<br>AND STAFFING
  </a>

  <section class="card" style="left:56px;width:282px">
    <h2>Our <span>IT Services</span></h2>
    <div class="rule"></div>
    <ul>
      <li>Pellentesque suscipit nisl a ligula</li>
      <li>Nunc et ipsum tortoreu</li>
      <li>Sed blandit leo eu tellus</li>
      <li>Vivamus feugiat egestas lacus</li>
      <li>Vestibulum in mauris sed massa</li>
      <li>Phasellus cursus convallis</li>
    </ul>
  </section>

  <section class="card staffing" style="left:374px;width:282px">
    <h2>Our <span>Staffing Services</span></h2>
    <div class="rule"></div>
    <p class="intro">Sed ut perspiciatis unde omnis iste natus error sit voluptatem accusantium dolor-emque laudantium.</p>
    <ul>
      <li>Vivamus feugiat egestas lacus</li>
      <li>Vestibulum in mauris sed massa</li>
      <li>Phasellus cursus convallis</li>
    </ul>
  </section>

  <section class="card" style="left:691px;width:381px">
    <h2>Our <span>Health Services</span></h2>
    <div class="rule"></div>
    <ul>
      <li>Phasellus cursus convallis lacus, id porttitor</li>
      <li>Vivamus feugiat egestas lacus, vitae pulvinar</li>
      <li>Sed blandit leo eu tellus mattis ornare</li>
      <li>Nunc et ipsum tortor, eu porta dolor</li>
      <li>Pellentesque suscipit nisl a ligula tristique</li>
      <li>Nam molestie pretium magna, nec facilisis</li>
    </ul>
  </section>

  <footer>
    <div class="footer-links">
      <a href="#">Home</a><span class="sep">|</span><a href="#">About Us</a><span class="sep">|</span><a href="#">Our services</a><span class="sep">|</span><a href="#">Our companies</a><span class="sep">|</span><a href="#">Latest News</a><span class="sep">|</span><a href="#">Contact us</a><span class="sep">|</span><a href="#">Member login</a><span class="sep">|</span><a href="#">Sitemap</a>
    </div>
    <div class="footer-copy">Copyright © 2012 www.brovana-group.com &nbsp; All rights reserved</div>
  </footer>
</body>
</html>
```